Business Card Design for an Investment Company

We need a business card design for our private investment company, called Ashbourne Partners. Ashbourne Partners is an investments partnership that aims to acquire shares in listed companies with a view to influencing those companies through active dialogue in order to improve their value. We need designs that use the logo colors (blue, grey, white), we need both English and Arabic on the business cards (can be on one side or 2 sides). The final logo should communicate professionalism, conservatism (nothing too fancy or too cheesy), that we are smart, conservative and old school.

Target Market(s)

Investment companies

Industry/Entity Type

Investment

Contact Information for Business Card

Khalid Yousef Rumaithi
Senior Executive Officer

Palm Terrace 07, Level 3, Office 215/12
HLMZ

+9714987650
krumaithi@ashbournepartners.com
www.ashbournepartners.com

Requirements
Must have
• Logo to be placed on the left hand side of the business card
• for the Arabic, we only need to have the name and title so it can be accomodated on one side so we can have the other side with full color and logo. The arabic that needs to be used is the below:
• خالد يوسف الرميثي
• المدير التنفيدي

```html
<!DOCTYPE html>
<html lang="en">
<head>
<meta charset="utf-8">
<title>Ashbourne Partners – Business Card</title>
<link rel="stylesheet" href="https://fonts.googleapis.com/css2?family=Roboto:wght@400;500;700&family=Noto+Kufi+Arabic:wght@400&display=swap">
<style>
  :root {
    --backdrop: #c9c9cb;
    --card-dark: #58585c;
    --card-light: #ffffff;
    --brand-blue: #1f6fa3;
    --text-grey: #4a4a4e;
    --text-white: #ffffff;
  }
  * { margin: 0; padding: 0; box-sizing: border-box; }
  html, body {
    width: 1200px; height: 1000px; overflow: hidden;
    background: var(--backdrop);
    font-family: "Roboto", Arial, sans-serif;
  }
  .canvas { position: relative; width: 1200px; height: 1000px; }
  .card {
    position: absolute; left: 269px; width: 663px; height: 380px;
    box-shadow: 0 3px 8px rgba(0,0,0,0.25);
  }
  .card--front { top: 108px; background: var(--card-dark); }
  .card--back { top: 520px; background: var(--card-light); }

  .front-wordmark {
    position: absolute; left: 0; right: 0; top: 162px;
    text-align: center; font-size: 40px; font-weight: 500;
    color: var(--text-white); letter-spacing: -0.5px;
  }
  .front-website {
    position: absolute; left: 0; right: 0; top: 319px;
    text-align: center; font-size: 17px; color: var(--text-white);
  }

  .back-wordmark {
    position: absolute; left: 37px; top: 38px;
    display: flex; align-items: center; gap: 12px;
    font-size: 38px; font-weight: 500; color: var(--brand-blue);
    letter-spacing: -0.5px;
  }
  .back-wordmark .mark {
    width: 14px; height: 14px; background: var(--text-grey);
  }

  .holder { position: absolute; left: 37px; top: 190px; }
  .holder-name { font-size: 19px; font-weight: 500; color: var(--brand-blue); }
  .holder-title { font-size: 14.5px; color: var(--text-grey); margin-top: 3px; }

  .holder-ar {
    position: absolute; right: 37px; top: 187px; text-align: right; direction: rtl;
    font-family: "Noto Kufi Arabic", "Tahoma", sans-serif;
  }
  .holder-ar-name { font-size: 16px; color: var(--brand-blue); }
  .holder-ar-title { font-size: 15px; color: var(--text-grey); margin-top: 2px; }

  .contact { position: absolute; left: 37px; top: 282px; list-style: none; }
  .contact li {
    display: flex; align-items: center; gap: 5px;
    font-size: 14.5px; color: var(--text-grey); line-height: 21px;
  }
  .contact svg { width: 11px; height: 11px; fill: var(--brand-blue); }

  .address {
    position: absolute; right: 37px; top: 282px; text-align: right;
    font-style: normal; font-size: 14.5px; color: var(--text-grey); line-height: 21.5px;
  }
</style>
</head>
<body>
<main class="canvas">
  <section class="card card--front" aria-label="Card front">
    <div class="front-wordmark">Ashbourne Partners</div>
    <div class="front-website">www.ashbournepartners.com</div>
  </section>

  <section class="card card--back" aria-label="Card back">
    <div class="back-wordmark"><span>Ashbourne Partners</span><span class="mark"></span></div>

    <div class="holder">
      <div class="holder-name">Khalid Yousef Rumaithi</div>
      <div class="holder-title">Senior Executive Officer</div>
    </div>

    <div class="holder-ar" lang="ar">
      <div class="holder-ar-name">خالد يوسف الرميثي</div>
      <div class="holder-ar-title">المدير التنفيدي</div>
    </div>

    <ul class="contact">
      <li>
        <svg viewBox="0 0 12 12" aria-hidden="true"><path d="M2.4 0.6 L4.4 2.8 L3.3 4.2 C4 5.7 5.9 7.7 7.6 8.6 L8.9 7.5 L11.3 9.5 L10 11.4 C6 11 1 6 0.6 2 Z"/></svg>
        +9714987650
      </li>
      <li>
        <svg viewBox="0 0 12 12" aria-hidden="true"><path d="M0.5 2.5 H11.5 V9.5 H0.5 Z M1.3 3.2 L6 6.6 L10.7 3.2 Z" fill-rule="evenodd"/></svg>
        krumaithi@ashbournepartners.com
      </li>
    </ul>

    <address class="address">
      Palm Terrace 07, Level 3<br>
      Office 215/12<br>
      HLMZ
    </address>
  </section>
</main>
</body>
</html>
```